Landing promo page for a Travel/Lifestyle app

Landing promotion page is needed for a new travel/Lifestyle app in English. We would like to have the logo of the company... and a brief info about our app, and two links to take you to Vintro Deck store or Kestrel Bazaar to download the app. One or several application screens can be shown.

Target Market(s)

Travel, leisure, holidays

Industry/Entity Type

Travel

Font styles to use
Sans Serif

Requirements
Must have
• logo, colors of the logo
• 2 buttons for vintro deck and kestrel bazaar
• screen shots of the app screen
• a brief introduction to the app (about 100 words) I'll post this later
• modern, fresh, minimalist, contemporary, clean,
Nice to have
• abstract design,
Should not have
• different colors of the logo or pictures of people or animals.

```html
<!DOCTYPE html>
<html lang="en">
<head>
<meta charset="utf-8">
<title>Roam Lark – Discover the World</title>
<link rel="stylesheet" href="https://fonts.googleapis.com/css2?family=Playfair+Display:wght@400;700&family=Poppins:wght@300;400;500;600&display=swap">
<style>
  :root {
    --ink: #3d4a5c;
    --ink-soft: #6b7380;
    --teal: #5ec2b2;
    --teal-deep: #4f9ea2;
    --purple: #4c4a92;
    --purple-deep: #433d80;
    --paper: #ffffff;
    --mist: #f4f4f4;
    --foot: #e9e9e9;
    --map: #ececec;
    --device: #f7f7f7;
    --device-edge: #d9d9d9;
    --black: #0e0e0e;
  }
  * { box-sizing: border-box; margin: 0; padding: 0; }
  html, body { width: 1200px; height: 2586px; overflow: hidden; }
  body {
    position: relative;
    background: var(--paper);
    color: var(--ink);
    font-family: "Poppins", sans-serif;
  }
  a { text-decoration: none; }
  .abs { position: absolute; }

  /* Hero */
  .hero-map {
    left: 535px; top: 0; width: 665px; height: 422px;
    background: linear-gradient(180deg, var(--map) 0%, #f3f3f3 60%, rgba(255,255,255,0) 100%);
  }
  .brand { left: 232px; top: 50px; display: flex; flex-direction: column; align-items: center; gap: 10px; }
  .brand-dot { width: 56px; height: 56px; border-radius: 50%; background: linear-gradient(135deg, var(--teal), var(--purple)); }
  .brand-name { font-family: "Playfair Display", serif; font-weight: 700; font-size: 17px; letter-spacing: 3px; color: var(--purple-deep); }
  .hero-title { left: 215px; top: 186px; font-size: 31px; line-height: 40px; letter-spacing: 1.5px; color: var(--ink); font-weight: 400; }
  .hero-title .light { font-family: "Poppins", sans-serif; font-weight: 300; }
  .hero-title .strong { font-family: "Playfair Display", serif; font-weight: 700; }
  .hero-sub { left: 215px; top: 288px; font-size: 16px; color: var(--ink); }
  .hero-cta { left: 215px; top: 342px; font-size: 16px; font-weight: 600; }

  .store { display: flex; align-items: center; gap: 8px; background: var(--black); color: #fff; border-radius: 6px; padding: 0 12px; white-space: nowrap; }
  .store-dot { width: 14px; height: 14px; border-radius: 50%; background: #fff; flex: none; }
  .store-text { display: flex; flex-direction: column; line-height: 1.1; }
  .store-text small { font-size: 8px; letter-spacing: .3px; }
  .store-text b { font-weight: 500; font-size: 12px; }
  .store.sm { height: 37px; }
  .store.lg { height: 47px; padding: 0 14px; }
  .store.lg .store-dot { width: 18px; height: 18px; }
  .store.lg small { font-size: 10px; }
  .store.lg b { font-size: 16px; }
  .hero-stores { left: 220px; top: 391px; display: flex; gap: 12px; }

  .phone { border-radius: 30px; background: var(--device); border: 2px solid var(--device-edge); box-shadow: 0 10px 30px rgba(0,0,0,.12); padding: 10px; }
  .screen { width: 100%; height: 100%; border-radius: 22px; background: linear-gradient(180deg, var(--teal) 0%, var(--purple) 100%); }

  /* Sections */
  .band-about { left: 0; top: 569px; width: 1200px; height: 376px; background: var(--mist); }
  .section-title { width: 1200px; left: 0; text-align: center; font-family: "Playfair Display", serif; font-weight: 400; font-size: 26px; letter-spacing: 1.5px; color: var(--ink); }
  .rule { left: 579px; width: 42px; height: 3px; background: var(--ink); }
  .about-copy { left: 285px; top: 666px; width: 630px; text-align: center; font-size: 11px; line-height: 17px; color: var(--ink-soft); }
  .about-copy p + p { margin-top: 13px; }
  .video-phone { left: 371px; top: 807px; width: 457px; height: 90px; border-radius: 18px; background: linear-gradient(90deg, #c9b79a, #e6dccb); padding: 6px 42px; box-shadow: 0 14px 24px rgba(0,0,0,.15); }
  .video-screen { width: 100%; height: 100%; background: linear-gradient(90deg, #2c3a35, #5d6a62 50%, #2f3b37); display: flex; align-items: center; justify-content: center; }
  .play { width: 36px; height: 36px; border-radius: 50%; border: 2px solid #fff; display: flex; align-items: center; justify-content: center; }

  .feature-list { left: 541px; top: 1116px; width: 390px; }
  .feature { margin-bottom: 46px; }
  .feature h3 { font-size: 11px; font-weight: 600; letter-spacing: .4px; color: var(--ink); margin-bottom: 18px; }
  .feature p { font-size: 10.5px; line-height: 17px; color: var(--ink-soft); }
  .feature em { font-weight: 600; color: var(--ink); }

  /* Call to action */
  .band-cta { left: 0; top: 1565px; width: 1200px; height: 269px; overflow: hidden; background: linear-gradient(180deg, var(--teal-deep) 0%, var(--purple-deep) 100%); }
  .cta-kicker { left: 215px; top: 40px; font-size: 16px; color: #fff; }
  .cta-title { left: 215px; top: 60px; font-size: 44px; line-height: 56px; font-weight: 600; color: #fff; }
  .cta-copy { left: 215px; top: 124px; width: 300px; font-size: 13px; line-height: 20px; color: #fff; }
  .cta-stores { left: 215px; top: 186px; display: flex; gap: 12px; }
  .tilted { border-radius: 26px; background: var(--device); border: 2px solid var(--device-edge); padding: 10px; }

  /* Screenshots */
  .shots-sub { width: 1200px; left: 0; top: 1958px; text-align: center; font-size: 13px; color: var(--ink); }
  .shot { border-radius: 12px; }
  .shot.grad { background: linear-gradient(180deg, var(--teal), var(--purple)); }
  .shot.pale { background: #f6f6f6; border: 1px solid #e6e6e6; }
  .shot.dark { background: #1a1a1a; padding: 9px; border-radius: 22px; }
  .arrow { width: 40px; height: 40px; border-radius: 50%; border: 1px solid #cfcfcf; background: #fff; display: flex; align-items: center; justify-content: center; }
  .dots { left: 569px; top: 2411px; display: flex; gap: 4px; }
  .dots span { width: 8px; height: 8px; border-radius: 50%; background: var(--teal); }
  .dots span:first-child { background: var(--purple-deep); }

  /* Footer */
  .footer { left: 0; top: 2465px; width: 1200px; height: 121px; background: var(--foot); }
  .social { top: 20px; width: 38px; height: 38px; border-radius: 50%; background: #5d6470; color: #fff; font-size: 14px; font-weight: 500; display: flex; align-items: center; justify-content: center; }
  .copyright { width: 1200px; left: 0; top: 85px; text-align: center; font-size: 9.5px; letter-spacing: .4px; color: var(--ink-soft); }
</style>
</head>
<body>

<!-- Hero -->
<div class="abs hero-map" role="img" aria-label="Faint world map with airplanes and city landmark skyline"></div>

<div class="abs brand">
  <span class="brand-dot"></span>
  <span class="brand-name">ROAM LARK</span>
</div>

<h1 class="abs hero-title">
  <span class="light">DISCOVER THE WORLD.</span><br>
  <span class="strong">SHARE YOUR JOURNEY.</span>
</h1>
<p class="abs hero-sub">Find, Save, and Share Your Favorite Travel Hot Spots.</p>
<p class="abs hero-cta">Download Now</p>

<div class="abs hero-stores">
  <a class="store sm">
    <span class="store-dot"></span>
    <span class="store-text"><small>Download on the</small><b>Kestrel Bazaar</b></span>
  </a>
  <a class="store sm">
    <span class="store-dot"></span>
    <span class="store-text"><small>GET IT ON</small><b>Vintro Deck</b></span>
  </a>
</div>

<div class="abs phone" style="left:712px;top:112px;width:176px;height:379px;" role="img" aria-label="Phone showing the app sign-in screen">
  <div class="screen"></div>
</div>

<!-- About -->
<div class="abs band-about"></div>
<h2 class="abs section-title" style="top:596px;">ABOUT ROAM LARK</h2>
<div class="abs rule" style="top:640px;"></div>
<div class="abs about-copy">
  <p>Looking to uncover the hidden gems when you travel? Download the hottest travel lifestyle app and find thousands of unique, cool things to see, do, and experience. Wherever you go in the world, Roam Lark is there.</p>
  <p>Whether you're a travel junkie, researching your next big adventure, or you're a casual tourist, trip planner, or even a business traveler—Roam Lark has all the restaurants, attractions, and sites you'll want to see.</p>
</div>
<div class="abs video-phone" role="img" aria-label="Landscape phone playing a video of a forest road">
  <div class="video-screen">
    <span class="play"><svg width="14" height="14" viewBox="0 0 14 14"><path d="M4 2 L12 7 L4 12 Z" fill="#fff"/></svg></span>
  </div>
</div>

<!-- Features -->
<h2 class="abs section-title" style="top:983px;">OUR FETURES</h2>
<div class="abs rule" style="top:1027px;"></div>
<div class="abs phone" style="left:267px;top:1083px;width:199px;height:370px;border-radius:26px;padding:46px 12px 58px;" role="img" aria-label="Phone showing the app splash screen">
  <div class="screen" style="border-radius:4px;"></div>
</div>
<div class="abs feature-list">
  <div class="feature">
    <h3>STAY ORGANIZED AT HOME AND ABROAD</h3>
    <p>Roam Lark lets you create lists of all the best places you want to visit. Create shared itineraries <em>(it's more about creating a list than itineraries)</em>, showcase the places you've been, or just dream up your perfect vacation with your friends and family.</p>
  </div>
  <div class="feature">
    <h3>NEVER HAVE A BORING VACATION AGAIN</h3>
    <p>With our unique discovery tools, you'll find all the cool places you'll need to have the best vacation ever. Cafes, art galleries, monuments, historical sites…no matter what you love to do, no matter where you go, Roam Lark can help you find them.</p>
  </div>
  <div class="feature">
    <h3>GET OUT OF THE RUT</h3>
    <p>Looking for inspiration? Experience new adventures every time you use Roam Lark. See what's hot in your area and save all your favorite places for later.</p>
  </div>
</div>

<!-- Call to action -->
<section class="abs band-cta">
  <p class="abs cta-kicker">What Are You Waiting For?</p>
  <h2 class="abs cta-title">Hop to It!</h2>
  <p class="abs cta-copy">Become a Roam Lark today by downloading our app.</p>
  <div class="abs cta-stores">
    <a class="store lg">
      <span class="store-dot"></span>
      <span class="store-text"><small>Download on the</small><b>Kestrel Bazaar</b></span>
    </a>
    <a class="store lg">
      <span class="store-dot"></span>
      <span class="store-text"><small>GET IT ON</small><b>Vintro Deck</b></span>
    </a>
  </div>
  <div class="abs tilted" style="left:720px;top:120px;width:240px;height:330px;transform:rotate(-28deg);" role="img" aria-label="Phone showing a city detail screen">
    <div class="screen" style="border-radius:16px;background:#fafafa;"></div>
  </div>
  <div class="abs tilted" style="left:900px;top:-40px;width:230px;height:330px;transform:rotate(22deg);" role="img" aria-label="Phone showing the explore bubble map">
    <div class="screen" style="border-radius:16px;background:#fafafa;"></div>
  </div>
</section>

<!-- Screenshots -->
<h2 class="abs section-title" style="top:1879px;">SCREENSHOTS</h2>
<div class="abs rule" style="top:1923px;"></div>
<p class="abs shots-sub">Please check screen shots how it works.</p>

<div class="abs arrow" style="left:151px;top:2162px;"><svg width="14" height="14" viewBox="0 0 14 14"><path d="M9 2 L4 7 L9 12" stroke="#444" stroke-width="2" fill="none"/></svg></div>
<div class="abs arrow" style="left:1004px;top:2162px;"><svg width="14" height="14" viewBox="0 0 14 14"><path d="M5 2 L10 7 L5 12" stroke="#444" stroke-width="2" fill="none"/></svg></div>

<div class="abs shot grad" style="left:252px;top:2090px;width:89px;height:196px;" role="img" aria-label="App splash screen"></div>
<div class="abs shot grad" style="left:367px;top:2055px;width:121px;height:259px;" role="img" aria-label="App travel quote screen"></div>
<div class="abs shot dark" style="left:517px;top:2017px;width:169px;height:336px;" role="img" aria-label="Featured app splash screen">
  <div class="screen" style="border-radius:14px;"></div>
</div>
<div class="abs shot pale" style="left:714px;top:2055px;width:122px;height:259px;" role="img" aria-label="App explore bubble map screen"></div>
<div class="abs shot pale" style="left:871px;top:2090px;width:93px;height:196px;" role="img" aria-label="App city detail screen"></div>

<div class="abs dots"><span></span><span></span><span></span><span></span><span></span></div>

<!-- Footer -->
<footer class="abs footer">
  <a class="abs social" style="left:552px;" aria-label="Chatterly">C</a>
  <a class="abs social" style="left:603px;" aria-label="Snapfold">S</a>
  <p class="abs copyright">© 2019, ALL RIGHTS RESERVED, ROAM LARK</p>
</footer>

</body>
</html>
```